Surgical Procedure Room Letterhead

PLEASE DO NOT MAKE YOUR LETTERHEAD SIMILAR TO THE ONE I AM INCLUDING IN MY UPLOADS

Hello! I need my logo used to make a very clean, professional, simple letterhead that has all the pertinent information in it:
Location: 4182 NW 38th Lane, Suite 500
Tamarac, FL 33967
Phone: 954-218-4650
Fax: 800-642-9082

Can you please put this all on a word document that is easily editable? I will include my practice letterhead as an example ONLY of how easy it should be to write below the letterhead. Please don't make this letterhead the same as the one I am including in this example. They are two separate businesses.

Target Market(s)

Insurance companies

Industry/Entity Type

medical

Requirements
Must have
• classiness, elegance, simplicity
Should not have
• Please don't make your letterhead the same as the one that I included in my uploads

```html
<!DOCTYPE html>
<html lang="en">
<head>
<meta charset="utf-8">
<title>Meridian Suites Letterhead</title>
<link rel="stylesheet" href="https://fonts.googleapis.com/css2?family=Manrope:wght@400;500;600;700&display=swap">
<style>
  :root {
    --navy: #0c2d57;
    --gold: #d4aa35;
    --ink: #555a60;
    --ink-dark: #1c1c1c;
    --rule: #d9d9d9;
    --backdrop: #e9eaec;
    --paper: #ffffff;
    --ghost: #f2f2f2;
    --sign-tone: #f3f3f3;
  }
  * { margin: 0; padding: 0; box-sizing: border-box; }
  html, body { width: 999px; height: 1200px; overflow: hidden; }
  body {
    background: var(--backdrop);
    font-family: "Manrope", Arial, sans-serif;
    color: var(--ink);
    position: relative;
  }
  .letterhead {
    position: absolute;
    left: 108px; top: 50px;
    width: 783px; height: 1100px;
    background: var(--paper);
    overflow: hidden;
  }
  .brand {
    position: absolute; left: 54px; top: 90px;
    display: flex; align-items: center; gap: 12px;
  }
  .brand-dot {
    width: 40px; height: 40px; border-radius: 50%;
    background: var(--gold);
  }
  .brand-name {
    font-size: 25px; font-weight: 700; color: var(--navy);
    line-height: 1.05; letter-spacing: 0.3px;
  }
  .company-contact {
    position: absolute; right: 57px; top: 72px;
    text-align: right; font-size: 14px; line-height: 18px;
    font-style: normal;
  }
  .contact-line { display: flex; justify-content: flex-end; align-items: center; gap: 5px; height: 26px; }
  .contact-icon { width: 16px; height: 16px; }
  .address { margin-top: 8px; line-height: 17px; }
  .header-rule {
    position: absolute; left: 54px; top: 203px;
    width: 672px; height: 1px; background: var(--rule);
  }
  .recipient { position: absolute; left: 54px; top: 295px; font-size: 14px; line-height: 25px; }
  .recipient-name { color: var(--gold); font-size: 20px; font-weight: 700; letter-spacing: 0.4px; margin-bottom: 2px; }
  .recipient-address { line-height: 19px; margin-top: 3px; }
  .date { position: absolute; right: 52px; top: 404px; font-size: 17px; font-weight: 600; }
  .body-copy {
    position: absolute; left: 54px; top: 448px; width: 677px;
    font-size: 15.5px; line-height: 24.4px; letter-spacing: 0.2px;
    text-align: justify; hyphens: auto;
  }
  .body-copy p + p { margin-top: 24px; }
  .signature {
    position: absolute; left: 566px; top: 820px;
    width: 120px; height: 66px;
    background: linear-gradient(180deg, transparent, var(--sign-tone) 50%, transparent);
  }
  .signatory {
    position: absolute; right: 67px; top: 900px;
    font-size: 22px; font-weight: 700; color: var(--ink-dark);
  }
  .ghost-mark { position: absolute; left: 160px; top: 920px; }
  .footer-band { position: absolute; left: 0; bottom: 0; }
</style>
</head>
<body>
  <main class="letterhead" lang="la">
    <div class="brand" lang="en">
      <span class="brand-dot"></span>
      <span class="brand-name">Meridian Suites</span>
    </div>

    <address class="company-contact" lang="en">
      <div class="contact-line">706-218-4650
        <svg class="contact-icon" viewBox="0 0 16 16"><rect width="16" height="16" rx="3" fill="var(--gold)"/><path d="M5 3.5l2 2-1 1.3c.6 1.3 1.6 2.3 2.9 2.9l1.3-1 2 2-1.3 1.6C7.6 12 4 8.4 3.6 4.9z" fill="#fff"/></svg>
      </div>
      <div class="contact-line">800-642-9082
        <svg class="contact-icon" viewBox="0 0 16 16"><rect width="16" height="16" rx="3" fill="var(--gold)"/><rect x="4" y="4" width="8" height="8" rx="1" fill="none" stroke="#fff" stroke-width="1.4"/><path d="M4 7h8" stroke="#fff" stroke-width="1.2"/></svg>
      </div>
      <div class="address">4182 NW 38th Lane, Suite 500<br>Fairhaven Bay, GA 30512</div>
    </address>

    <div class="header-rule"></div>

    <section class="recipient" lang="en">
      <div class="recipient-name">DANA WHITFIELD</div>
      <div>0147-382-615</div>
      <div>hello@meridiansuites.net</div>
      <div class="recipient-address">2087 Harbor View Rd. Suite<br>214 Austin, TX 78701</div>
    </section>

    <div class="date" lang="en">12 December, 2024</div>

    <article class="body-copy">
      <p>Lorem ipsum dolor sit amet, consectetuer adipiscing elit, sed diam nonummy nibh euismod tincidunt ut laoreet dolore magna aliquam erat volutpat. Ut wisi enim ad minim veniam, quis nostrud exerci tation ullamcorper suscipit lobortis nisl ut aliquip ex ea commodo consequat. Duis autem vel eum iriure dolor in hendrerit in vulputate velit esse molestie consequat, vel illum dolore eu feugiat nulla facilisis at vero eros et accumsan et iusto odio dignissim qui blandit praesent luptatum zzril delenit augue duis dolore te feugait nulla facilisi.</p>
      <p>Lorem ipsum dolor sit amet, cons ectetuer adipiscing elit, sed diam nonummy nibh euismod tincidunt ut laoreet dolore magna aliquam erat volutpat. Ut wisi enim ad minim veniam, quis nostrud exerci tation ullamcorper suscipit lobortis nisl ut aliquip ex ea commodo consequat.</p>
    </article>

    <div class="signature" role="img" aria-label="Handwritten signature"></div>
    <div class="signatory" lang="en">Mr. Dana Whitfield</div>

    <svg class="ghost-mark" width="200" height="200" viewBox="0 0 200 200" aria-hidden="true">
      <circle cx="100" cy="100" r="88" fill="none" stroke="var(--ghost)" stroke-width="12"/>
    </svg>

    <svg class="footer-band" width="783" height="16" viewBox="0 0 783 16" aria-hidden="true">
      <polygon points="352,0 783,0 783,16 346,16" fill="var(--navy)"/>
    </svg>
  </main>
</body>
</html>
```